GravaLoop. Customer needs to know about us, what services we provide & contact us

We are a waste tire recycling company. Our primary focus is on providing a sustainable and cost effective service focusing on: Waste Tire Management, Hassle Free Scheduling for Tire Collection, Mobile Shredding & Special site cleanup services. GravaLoop will be producing TDF, Clean Tire Wire & further materials.
Please look at https://harvonrubber.example
Please look at https://quelbamaterials.example

This is the look and feel of what we want

I have attached a word document with our website info.

Target Market(s)

Tire Install Companies. Such as morbanhaul.example. TDF Purchasers such as pelkofuel.example.

Industry/Entity Type

Waste Tire Recycling

Coding

Coded - Design and coding required

Number of Pages Required

3 page

Font styles to use
Other font styles liked:
• Look at our logo

Requirements
Must have
• We need a 3 page setup for About Us, Services & Contact Us. Contact us should be a form them can fill out and submit to us Images that are related to waste tire recycling. Clean, modern, innovative.
Nice to have
• The color and feel of the website should work with our logo that we did with artpivot
Should not have
• Anything progressive, political or "woke"

```html
<!DOCTYPE html>
<html lang="en">
<head>
<meta charset="utf-8">
<title>GravaLoop – Waste Tire Recycling</title>
<link href="https://fonts.googleapis.com/css2?family=Poppins:wght@400;500;600;700;800&display=swap" rel="stylesheet">
<style>
:root{
  --green:#1e9a3a;
  --green-dark:#157a2c;
  --ink:#222;
  --muted:#555;
  --dark:#1b1b1b;
  --dark-2:#2a2a2a;
  --light:#f1f1f1;
  --white:#fff;
}
*{box-sizing:border-box;margin:0;padding:0}
html,body{width:1200px;height:4175px;overflow:hidden}
body{font-family:'Poppins',sans-serif;color:var(--ink);background:var(--white);position:relative}
.abs{position:absolute}
.btn{position:absolute;display:flex;align-items:center;background:var(--green);color:var(--white);font-weight:600;font-size:14px;border-radius:24px;padding-left:26px}
.btn .ring{position:absolute;right:4px;top:50%;transform:translateY(-50%);width:30px;height:30px;border-radius:50%;background:var(--white);border:2px solid var(--green);display:flex;align-items:center;justify-content:center}
.label{color:var(--green);font-weight:600;font-size:20px}
.label::after{content:" ›";font-weight:700}
.heading{font-weight:600;font-size:34px;color:var(--ink)}
.heading em{font-style:normal;color:var(--green)}
.placeholder{position:absolute}
.brand{font-weight:800;font-size:34px;color:var(--green);display:flex;align-items:center;gap:10px;letter-spacing:-.5px}
.brand .dot{width:22px;height:22px;border-radius:50%;background:var(--green)}

/* header */
.topbar{top:8px;left:620px;font-size:13px;color:var(--ink);display:flex;gap:60px}
.nav{top:52px;left:607px;display:flex;gap:48px;font-size:14px;font-weight:500}
.nav span::after{content:" ›";color:#aaa}

/* hero */
.hero{top:107px;left:0;width:1200px;height:530px;background:linear-gradient(135deg,#2c2c2c,#111 70%)}
.hero-text{top:135px;left:72px;color:var(--white)}
.hero-text .pre{font-size:22px;display:flex;align-items:center;gap:10px}
.hero-text .pre::before{content:"";width:62px;height:1px;background:var(--white)}
.hero-text h1{font-weight:800;font-size:48px;line-height:55px;margin-top:16px}
.hero-text p{font-size:20px;line-height:33px;margin-top:20px;width:500px}

/* services */
.services{top:1207px;left:0;width:1200px;height:1098px;background:var(--light)}
.card{position:absolute;background:var(--white);width:484px;height:425px}
.card h3{position:absolute;font-weight:600;font-size:21px;line-height:32px;width:220px}
.card p{position:absolute;font-size:13px;line-height:24px;width:235px;color:var(--muted)}
.card a{position:absolute;font-size:13px;font-weight:600;color:var(--ink);text-decoration:underline}

/* stats */
.stats{top:2305px;left:0;width:1200px;height:585px;background:linear-gradient(180deg,#222,#161616)}
.feature{position:absolute;width:330px;text-align:center;color:var(--white)}
.feature h4{font-weight:600;font-size:17px;margin-top:14px}
.feature p{font-size:13px;line-height:23px;color:#bbb;margin-top:8px}
.divider{position:absolute;width:1px;height:170px;background:#444}

/* testimonial */
.tab{position:absolute;left:72px;width:265px;height:113px;display:flex;align-items:center;padding-left:35px;gap:20px}
.tab .avatar{width:72px;height:72px;background:linear-gradient(#8a7563,#4d4038)}
.tab b{display:block;font-weight:600;font-size:18px}
.tab small{font-size:13px}
.quote{position:absolute;left:431px;top:3072px;width:697px;height:235px;border:2px solid #ddd;padding:28px 34px}

/* footer */
.footer{top:3655px;left:0;width:1200px;height:490px;background:linear-gradient(135deg,#1e1e1e,#141414)}
.footer h5{position:absolute;color:var(--white);font-weight:600;font-size:16px}
.offer li{list-style:none;color:var(--white);font-size:13px;line-height:19px;padding-left:26px;position:relative;margin-bottom:22px;width:210px}
.offer li::before{content:"›";position:absolute;left:6px;color:var(--white);font-weight:700}
.field{position:absolute;background:var(--white);font-size:11px;color:var(--muted);padding:10px 8px}
.copy{top:4145px;left:0;width:1200px;height:30px;background:var(--green);color:var(--white);font-size:12px;display:flex;align-items:center;justify-content:center}
</style>
</head>
<body>

<!-- header -->
<div class="abs brand" style="top:30px;left:73px"><span class="dot"></span>GravaLoop</div>
<div class="abs topbar">
  <span>☏ 555-014-2290 or Toll Free 800-555-0147</span>
  <span>✉ hello@gravaloop.example</span>
</div>
<nav class="abs nav"><span>About Us</span><span>Services</span><span>Contact Us</span></nav>
<div class="btn" style="top:40px;left:973px;width:155px;height:42px">Contact Us<span class="ring"></span></div>

<!-- hero -->
<section class="abs hero">
  <div class="placeholder" role="img" aria-label="Tire with green recycling arrows and tire tread marks" style="left:630px;top:0;width:570px;height:530px;background:radial-gradient(circle at 55% 50%,#2a7a3a,#1f1f1f 60%,transparent 75%)"></div>
  <div class="abs hero-text">
    <div class="pre">We Are A</div>
    <h1>Waste Tire<br>Recycling Company</h1>
    <p>Our primary focus is on providing a sustainable and cost effective service</p>
  </div>
  <div class="btn" style="top:388px;left:72px;width:155px;height:42px">Get A Service<span class="ring"></span></div>
</section>

<!-- about -->
<div class="abs" style="top:697px;left:72px;width:352px;height:453px;background:var(--green)"></div>
<div class="placeholder" role="img" aria-label="Rows of old tires laid out on a field" style="top:723px;left:124px;width:396px;height:394px;background:linear-gradient(180deg,#7a8f5a 0%,#9aa27a 25%,#3d3d38 60%,#2c2c28)"></div>
<div class="abs label" style="top:786px;left:612px;font-size:19px">About</div>
<h2 class="abs heading" style="top:815px;left:612px;font-size:32px">Do You Know <em>Us?</em></h2>
<p class="abs" style="top:878px;left:612px;width:515px;font-size:14px;line-height:28px;color:var(--muted)">GravaLoop is forging the way towards a more sustainable future through scrap tire collection &amp; waste tire recycling. You've got a business to run, and we've got you covered. Let us worry about your scrap tire removal so you don't have to. Through the use of innovative technologies.</p>
<div class="btn" style="top:1008px;left:612px;width:155px;height:44px">Learn More<span class="ring"></span></div>

<!-- services -->
<section class="abs services">
  <div class="abs label" style="top:64px;left:0;width:1200px;text-align:center">Services</div>
  <h2 class="abs heading" style="top:93px;left:0;width:1200px;text-align:center">We Are Qualified &amp; For <em>Services</em></h2>

  <div class="card" style="top:163px;left:104px">
    <h3 style="top:80px;left:236px">Waste Tire Management &amp; Recycling</h3>
    <p style="top:196px;left:236px">Our priority is our core focus on providing our clients with industry leading waste tire management services.</p>
    <a style="top:305px;left:236px">Learn More</a>
  </div>
  <div class="placeholder" role="img" aria-label="Gloved hand holding shredded tire rubber" style="top:201px;left:71px;width:245px;height:350px;background:linear-gradient(160deg,#555,#2e2e2e 50%,#3a6fa8 70%,#555)"></div>

  <div class="card" style="top:163px;left:644px">
    <h3 style="top:80px;left:236px">Tire Remediation &amp; Special Tire Clean-Ups</h3>
    <p style="top:196px;left:236px">GravaLoop's core business was derived from our handling of special tire clean up situations. These abandoned or neglected.</p>
    <a style="top:305px;left:236px">Learn More</a>
  </div>
  <div class="placeholder" role="img" aria-label="Mechanic mounting a tire in a workshop" style="top:201px;left:611px;width:245px;height:350px;background:linear-gradient(180deg,#cfcfcf,#6d6d6d 45%,#1f1f1f 75%,#7a2020)"></div>

  <div class="card" style="top:615px;left:104px">
    <h3 style="top:80px;left:236px">Scheduling &amp; Billing</h3>
    <p style="top:164px;left:236px">GravaLoop is here to make your day-to-day easier with a seamless scheduling program. We pride ourselves in prompt.</p>
    <a style="top:273px;left:236px">Learn More</a>
  </div>
  <div class="placeholder" role="img" aria-label="Hands writing on billing papers" style="top:653px;left:71px;width:245px;height:350px;background:linear-gradient(150deg,#f2efea,#d9d4cc 50%,#b8b1a6)"></div>

  <div class="card" style="top:615px;left:644px">
    <h3 style="top:80px;left:236px">First Rate Customer Support &amp; Service</h3>
    <p style="top:164px;left:236px">At GravaLoop our customer is our priority. We have built a team that shares in our commitment to excellence and shares.</p>
    <a style="top:273px;left:236px">Learn More</a>
  </div>
  <div class="placeholder" role="img" aria-label="Customer support agent with headset" style="top:653px;left:611px;width:245px;height:350px;background:linear-gradient(180deg,#eee,#c9b8a8 45%,#2a2a2a 85%)"></div>
</section>

<!-- stats -->
<section class="abs stats">
  <div class="abs label" style="top:62px;left:0;width:1200px;text-align:center">Tires Recycles</div>
  <h2 class="abs" style="top:94px;left:0;width:1200px;text-align:center;color:var(--white);font-weight:600;font-size:32px">Providing Great Service Fuels Our Growth.</h2>
  <div class="abs" style="top:140px;left:0;width:1200px;text-align:center;font-weight:800;font-size:78px;color:#cfcfcf;letter-spacing:2px">1,000,000</div>

  <div class="feature" style="top:260px;left:83px">
    <svg width="50" height="50" viewBox="0 0 50 50" fill="none" stroke="var(--green)" stroke-width="2.5"><path d="M25 45V22M25 22C25 10 14 6 6 6c0 10 8 16 19 16zM25 22c0-12 11-16 19-16 0 10-8 16-19 16z"/></svg>
    <h4>Eco Friendly</h4>
    <p>There are many variations of passages of Lorem Ipsum available, but the majority have suffered.</p>
  </div>
  <div class="divider" style="top:280px;left:420px"></div>
  <div class="feature" style="top:260px;left:435px">
    <svg width="50" height="50" viewBox="0 0 50 50" fill="none" stroke="var(--green)" stroke-width="2.5"><circle cx="25" cy="22" r="12"/><path d="M25 4v6M25 34v12M7 22h6M37 22h6M12 9l4 4M38 9l-4 4"/></svg>
    <h4>Innovative Technology</h4>
    <p>There are many variations of passages of Lorem Ipsum available, but the majority have suffered.</p>
  </div>
  <div class="divider" style="top:280px;left:780px"></div>
  <div class="feature" style="top:260px;left:795px">
    <svg width="50" height="50" viewBox="0 0 50 50" fill="none" stroke="var(--green)" stroke-width="2.5"><circle cx="25" cy="25" r="20"/><circle cx="25" cy="25" r="9"/><path d="M25 5v11M25 34v11M5 25h11M34 25h11"/></svg>
    <h4>Unparalled Services</h4>
    <p>There are many variations of passages of Lorem Ipsum available, but the majority have suffered.</p>
  </div>
  <div class="btn" style="top:482px;left:523px;width:155px;height:42px">Join Us Now<span class="ring"></span></div>
</section>

<!-- testimonial -->
<div class="abs label" style="top:2960px;left:0;width:1200px;text-align:center">Testimonial</div>
<h2 class="abs heading" style="top:2990px;left:0;width:1200px;text-align:center">What People <em>Say</em></h2>
<div class="tab" style="top:3072px;background:var(--green);color:var(--white)"><span class="avatar" role="img" aria-label="Client portrait"></span><div><b>Dario Venn</b><small>Chef Leader</small></div></div>
<div class="tab" style="top:3192px;background:var(--light);border:1px solid #ddd"><span class="avatar" role="img" aria-label="Client portrait"></span><div><b>Dario Venn</b><small>Chef Leader</small></div></div>
<svg class="abs" style="top:3155px;left:368px" width="30" height="68" viewBox="0 0 30 68"><circle cx="15" cy="15" r="14" fill="var(--green)"/><path d="M9 18l6-6 6 6" stroke="#fff" stroke-width="2.5" fill="none"/><circle cx="15" cy="53" r="14" fill="#222"/><path d="M9 50l6 6 6-6" stroke="#fff" stroke-width="2.5" fill="none"/></svg>
<div class="quote">
  <p style="font-weight:500;font-size:17px;line-height:30px;width:560px">Long established fact that a reader will be distracted by the readable content .</p>
  <p style="font-size:13px;line-height:24px;color:var(--muted);margin-top:12px;width:600px">There are many variations of passages of Lorem Ipsum available, but the majority have suffered alteration in some form, by injected humour, or randomised words which don't look even slightly believable.</p>
  <p style="color:#f2b600;font-size:16px;margin-top:6px">★★★★☆</p>
  <span style="position:absolute;right:34px;bottom:10px;font-size:90px;color:#e6e6e6;line-height:1">”</span>
</div>

<!-- map + contact -->
<div class="placeholder" role="img" aria-label="Road map of the southern United States" style="top:3385px;left:0;width:1200px;height:270px;background:linear-gradient(90deg,#dfe8dc,#a8cf9a 40%,#9fcc8d 70%,#d7e6d2)"></div>
<div class="abs" style="top:3420px;left:72px;width:390px;height:200px;background:#2f2f2f;color:var(--white);padding:38px 26px">
  <div style="font-weight:600;font-size:20px">Contact Us ›</div>
  <p style="font-size:12px;line-height:21px;margin-top:14px;padding-left:18px;position:relative"><span style="position:absolute;left:0;color:var(--green)">●</span>Corporate Office 410 N Ridge Rd,<br>Ste 12 Fernvale, AZ</p>
  <p style="font-size:12px;margin-top:10px;padding-left:18px;position:relative"><span style="position:absolute;left:0;color:var(--green)">✉</span>contact@gravaloop.example</p>
</div>
<div class="btn" style="top:3573px;left:286px;width:155px;height:42px">Contact Us<span class="ring"></span></div>

<!-- footer -->
<footer class="abs footer">
  <div class="abs brand" style="top:95px;left:72px;color:var(--white);font-size:40px"><span class="dot" style="background:var(--white)"></span>GravaLoop</div>
  <svg class="abs" style="top:210px;left:72px" width="28" height="28" viewBox="0 0 28 28"><circle cx="14" cy="14" r="14" fill="var(--green)"/><path d="M9 8c1 5 5 10 10 12l2-3-3-2-2 2c-2-1-4-3-5-5l2-2-2-3z" fill="#fff"/></svg>
  <div class="abs" style="top:210px;left:110px;color:var(--white);font-size:13px">24/7 Emergency Roadside Service:</div>
  <div class="abs" style="top:230px;left:110px;color:var(--green);font-size:18px;font-weight:500">555-019-944</div>
  <div class="abs" style="top:273px;left:72px;width:320px;height:1px;background:#444"></div>
  <div class="abs" style="top:283px;left:72px;color:var(--white);font-size:13px">Follow Us :</div>
  <div class="abs" style="top:280px;left:155px;display:flex;gap:18px"><span style="width:22px;height:22px;border-radius:50%;background:#ddd"></span><span style="width:22px;height:22px;border-radius:50%;background:#ddd"></span><span style="width:22px;height:22px;border-radius:50%;background:#ddd"></span><span style="width:22px;height:22px;border-radius:50%;background:#ddd"></span></div>
  <div class="abs" style="top:318px;left:72px;width:320px;height:1px;background:#444"></div>
  <div class="abs" style="top:340px;left:72px;color:var(--white);font-size:13px">Get In Touch And Stay In Touch</div>
  <div class="abs" style="top:365px;left:72px;width:275px;height:38px;background:var(--white);border-radius:20px;font-size:12px;color:var(--muted);padding:11px 16px">Enter Your Mail ID</div>
  <div class="btn" style="top:369px;left:245px;width:98px;height:30px;font-size:13px;padding-left:16px">Subscribe</div>

  <h5 style="top:112px;left:427px">What We Offer</h5>
  <ul class="abs offer" style="top:148px;left:427px">
    <li>Waste Tire Management &amp; Recycling</li>
    <li>Tire Remediation &amp; Special Tire Clean-Ups</li>
    <li>Scheduling &amp; Billing</li>
    <li>First Rate Customer Support &amp; Service</li>
  </ul>

  <h5 style="top:112px;left:708px">Get In Touch</h5>
  <div class="field" style="top:152px;left:708px;width:210px;height:35px">Name</div>
  <div class="field" style="top:152px;left:921px;width:207px;height:35px">Email</div>
  <div class="field" style="top:190px;left:708px;width:210px;height:35px">Phone</div>
  <div class="field" style="top:190px;left:921px;width:207px;height:35px">Address of Business for PickUp</div>
  <div class="field" style="top:229px;left:708px;width:420px;height:107px">Message</div>
  <div class="btn" style="top:360px;left:705px;width:155px;height:42px">Submit Now<span class="ring"></span></div>
</footer>
<div class="abs copy">© 2022&nbsp;<span style="color:#d8f5c0">gravaloop</span>. All right Reserved</div>

</body>
</html>
```